New Website Design (Uncoded) Competition for Lorvex Trade Link

Please submit design concepts for a Joomla 3.0 Website for LORVEX TRADE LINK company. Our client prefers a modem style design, responsive to all mobile devices,
The website demo content needs to be clear and detailed.

Menu sample:
Home/About Us/Service/Strength/Partner/News/Contact US/Blog

Requirements:
1. Only need to submit the PSD for the design, coding work is not included.
2. Please submit both Homepage and Inner page to demonstrate the concept.
3. The Homepage needs to include: LOGO/MENU/Banner/Language Switcher/Company Introduction/Welcome module/Advertising Module/Footer Menu/Footer/Copyright/Social Links
4. Use Asian business women for demo pictures/Could try city pictures for background.
5. Prefer SINGLE SCREEN design rather than scrollable multiple screen designs.
6. Avoid any chain symbol since the company is more about financial business.
7. Avoid any direct connotations related with money or cash.
Updates

Hi Designers, I have clearly state the requirements that avoid using neg connontation pictures like cash/ property, though still receive concepts like that. Please check the brief clearly and mark at Update with "cheers" Kel from VT

Target Market(s)

Dongrui Lorvex Trade link Company provide cross-border Supply chain Financial service by integrating Dongrui Trade Link resource.
The Company mission is become the most respectful, professional and valuable Chinese Supply Chain Financial Company, pioneer the supply chain industry.

Industry/Entity Type

Financial

Font styles to use
Sans Serif

Colors
33b7a4

Requirements
Must have
• 1. Necessary Web element, including Logo/navigation/ Banner/ Footer
2. Asia business Women pictures.
Should not have
• 6. Avoid any chain symbol since the company is more about financial business.

```html
<!DOCTYPE html>
<html lang="en">
<head>
<meta charset="utf-8">
<title>Lorvex Trade Link</title>
<link rel="stylesheet" href="https://fonts.googleapis.com/css2?family=Arimo:wght@400;700&family=Open+Sans:wght@400;600&display=swap">
<style>
:root{
  --brand-blue:#0b7fc0;
  --phone-blue:#0a6fb0;
  --nav-top:#2bb4ea;
  --nav-bottom:#0c93d0;
  --tab-blue:#1aa0de;
  --ad-blue:#1a9fd9;
  --text-dark:#222;
  --text-body:#666;
  --logo-grey:#3d3d3d;
  --footer-bg:#2b2b2b;
  --footer-text:#f2f2f2;
  --footer-brand:#141414;
}
*{box-sizing:border-box;margin:0;padding:0}
html,body{width:1200px;height:1126px;overflow:hidden;background:#fff}
body{position:relative;font-family:Arimo,Arial,sans-serif;color:var(--text-dark)}
.abs{position:absolute}
.top-line{left:0;top:0;width:1200px;height:4px;background:var(--brand-blue)}
.brand{display:flex;align-items:center;gap:12px}
.brand .mark{width:34px;height:34px;background:var(--brand-blue)}
.brand .name{font-family:"Open Sans",sans-serif;font-weight:600;font-size:26px;color:var(--logo-grey);letter-spacing:.5px;white-space:nowrap}
.header-brand{left:134px;top:30px}
.lang{left:896px;top:27px;display:flex;align-items:center;gap:13px;font-size:14.5px;color:var(--brand-blue)}
.lang svg{display:block}
.phone{left:842px;top:64px;width:193px;height:29px;border-radius:15px;background:var(--phone-blue);color:#fff;display:flex;align-items:center;gap:10px;padding-left:12px;font-size:22px}
.hero{left:0;top:107px;width:1200px;height:410px;
  background:
    radial-gradient(ellipse 420px 120px at 620px 250px,rgba(255,230,170,.35),transparent 70%),
    radial-gradient(ellipse 260px 90px at 300px 290px,rgba(255,220,160,.28),transparent 70%),
    radial-gradient(ellipse 300px 110px at 960px 280px,rgba(255,210,170,.25),transparent 70%),
    radial-gradient(ellipse 500px 120px at 600px 420px,rgba(255,200,120,.22),transparent 70%),
    linear-gradient(180deg,#2f4fc0 0%,#4866cc 28%,#3b4fa0 46%,#1a1f3c 60%,#0e1226 68%,#1f2a5a 82%,#2a3a86 100%)}
.nav{left:132px;top:126px;width:957px;height:41px;border-radius:3px;background:linear-gradient(180deg,var(--nav-top),var(--nav-bottom));display:flex;padding-left:10px}
.nav a{color:#fff;text-decoration:none;font-size:14.4px;line-height:41px;padding:0 14px;border-right:1px solid rgba(255,255,255,.35)}
.nav a:last-child{border-right:none}
.slide-arrow{width:60px;height:60px;border-radius:50%;background:rgba(255,255,255,.25);display:flex;align-items:center;justify-content:center}
.caption{left:125px;top:461px;width:629px;height:36px;background:rgba(20,20,30,.55);color:#fff;font-family:"Open Sans",sans-serif;font-size:17px;line-height:36px;padding-left:22px}
.dots{left:640px;top:473px;display:flex;gap:7px}
.dots span{width:13px;height:13px;border-radius:50%;background:#bbb;border:1px solid #eee}
.dots span.on{background:var(--brand-blue)}
.tab{height:28px;width:213px;background:var(--tab-blue);color:#fff;font-size:12.5px;display:flex;align-items:center;gap:12px;padding-left:8px}
.tab .dot{width:16px;height:16px;border-radius:50%;background:#fff}
.tab.news{font-size:13px}
.card-img{width:194px;height:71px;border:1px solid #aaa}
.card-text{width:215px;font-size:14px;line-height:17.5px;color:var(--text-dark)}
.more{font-size:11.5px;color:var(--text-dark)}
.news-intro{left:856px;top:559px;width:240px;font-size:13.4px;line-height:17.5px;color:var(--text-dark)}
.field-label{font-size:13px;color:var(--text-dark)}
.field{width:143px;height:22px;border:1px solid #888;border-radius:2px;background:#fff}
.submit{left:908px;top:683px;width:59px;height:17px;border-radius:3px;background:#777;color:#fff;font-size:12.5px;text-align:center;line-height:17px}
.welcome-mark{left:138px;top:727px;width:30px;height:30px;background:var(--brand-blue)}
.welcome-title{left:194px;top:737px;font-family:"Open Sans",sans-serif;font-weight:400;font-size:18px;color:var(--text-dark)}
.welcome-img{left:133px;top:778px;width:240px;height:143px;border:2px solid #bbb;
  background:linear-gradient(180deg,#c9c5bb 0%,#9b958a 22%,#6f695f 38%,#d6d2ca 42%,#8a857b 55%,#4b4740 78%,#2b2824 100%)}
.body-copy{font-size:12.6px;line-height:17.4px;color:var(--text-body)}
.read-more{left:768px;top:966px;font-size:11.5px;color:var(--text-dark)}
.ad-title{left:875px;top:742px;width:160px;text-align:center;font-size:17px;color:var(--ad-blue)}
.ad-img{left:875px;top:768px;width:160px;height:223px;
  background:
    radial-gradient(ellipse 45px 60px at 80px 95px,rgba(200,215,215,.9),transparent 75%),
    linear-gradient(180deg,#f2f1e4 0%,#e8e8da 62%,#ffffff 70%,#2b7f7a 72%,#e9ece6 75%,#d6ddd8 100%)}
.view-all{left:981px;top:995px;font-size:12px;color:var(--text-dark)}
.footer{left:0;top:1026px;width:1200px;height:100px;background:var(--footer-bg)}
.footer-nav{left:134px;top:1046px;display:flex}
.footer-nav a{color:var(--footer-text);text-decoration:none;font-size:12px;margin-right:26px}
.copyright{left:145px;top:1092px;color:var(--footer-text);font-size:12.2px}
.footer-brand{left:842px;top:1056px}
.footer-brand .mark{background:var(--footer-brand)}
.footer-brand .name{color:var(--footer-brand);font-size:22px}
</style>
</head>
<body>
<div class="abs top-line"></div>

<header>
  <div class="abs brand header-brand"><span class="mark"></span><span class="name">LORVEX TRADE LINK</span></div>
  <div class="abs lang">
    <svg width="24" height="16" viewBox="0 0 24 16" aria-hidden="true"><rect width="24" height="16" fill="#1f3a8a"/><path d="M0 0L24 16M24 0L0 16" stroke="#fff" stroke-width="3"/><path d="M12 0V16M0 8H24" stroke="#fff" stroke-width="5"/><path d="M12 0V16M0 8H24" stroke="#d2232a" stroke-width="3"/></svg>
    <span>English</span>
  </div>
  <div class="abs phone">
    <svg width="20" height="20" viewBox="0 0 20 20" aria-hidden="true"><circle cx="10" cy="10" r="9" fill="none" stroke="#fff" stroke-width="1.6"/><path d="M7 5.5l1.6 2.4-1 1.2c.7 1.4 1.6 2.3 3 3l1.2-1 2.4 1.6-.9 1.7c-3.5-.3-6.7-3.5-7-7z" fill="#fff"/></svg>
    <span>555-0190-274</span>
  </div>
</header>

<section class="abs hero" role="img" aria-label="Night city skyline with lit towers reflected in a river"></section>
<nav class="abs nav">
  <a href="#">Home</a><a href="#">About Us</a><a href="#">Service</a><a href="#">Strength</a><a href="#">Partner</a><a href="#">News</a><a href="#">Contact US</a><a href="#">Blog</a>
</nav>
<div class="abs slide-arrow" style="left:115px;top:252px"><svg width="20" height="30" viewBox="0 0 20 30" aria-hidden="true"><path d="M14 4L5 15l9 11" fill="none" stroke="#fff" stroke-width="4"/></svg></div>
<div class="abs slide-arrow" style="left:1018px;top:252px"><svg width="20" height="30" viewBox="0 0 20 30" aria-hidden="true"><path d="M6 4l9 11-9 11" fill="none" stroke="#fff" stroke-width="4"/></svg></div>
<div class="abs caption">VOLTARA Heating and cooling Services.</div>
<div class="abs dots"><span class="on"></span><span></span><span></span><span></span><span></span></div>

<section class="services">
  <div class="abs tab" style="left:132px;top:526px"><span class="dot"></span>Superannuation</div>
  <div class="abs card-img" style="left:137px;top:560px;background:linear-gradient(160deg,#f1ead4 0%,#e2d7b6 35%,#f5f1e6 55%,#c9bd98 80%,#a89c7c 100%)" role="img" aria-label="Pension plan statement papers"></div>
  <p class="abs card-text" style="left:135px;top:641px">lorem ipsum dolor sit amet dolor, consecteture adipiscing elit.</p>
  <span class="abs more" style="left:147px;top:688px">More &gt;</span>

  <div class="abs tab" style="left:372px;top:526px"><span class="dot"></span>Retirement planning</div>
  <div class="abs card-img" style="left:378px;top:560px;background:linear-gradient(130deg,#3f7fd0 0%,#2a63b8 40%,#1c4a94 55%,#e3c21e 60%,#f0d23a 70%,#1c4a94 78%,#173f80 100%)" role="img" aria-label="Retirement ahead road sign against blue sky"></div>
  <p class="abs card-text" style="left:374px;top:641px">lorem ipsum dolor sit amet dolor, consecteture adipiscing elit.</p>
  <span class="abs more" style="left:378px;top:688px">More &gt;</span>

  <div class="abs tab" style="left:612px;top:526px"><span class="dot"></span>Budgeting and investments</div>
  <div class="abs card-img" style="left:618px;top:560px;background:linear-gradient(135deg,#7d8770 0%,#a8ae9c 25%,#eef0f2 45%,#f8f9fb 60%,#b4b9aa 80%,#6f7a64 100%)" role="img" aria-label="Investment chart on a desk"></div>
  <p class="abs card-text" style="left:617px;top:641px">lorem ipsum dolor sit amet dolor, consecteture adipiscing elit.</p>
  <span class="abs more" style="left:625px;top:688px">More &gt;</span>

  <div class="abs tab news" style="left:853px;top:526px"><span class="dot"></span>NEWSLETTERS SIGN UP</div>
  <p class="abs news-intro">Get news alerts! Watch new presentation Video and more stuff!</p>
  <span class="abs field-label" style="left:858px;top:611px">Name</span>
  <div class="abs field" style="left:907px;top:610px"></div>
  <span class="abs field-label" style="left:857px;top:645px">Email</span>
  <div class="abs field" style="left:907px;top:642px"></div>
  <div class="abs submit">Submit</div>
</section>

<section class="welcome">
  <div class="abs welcome-mark"></div>
  <h1 class="abs welcome-title">Welcome to Lorvex Trade Link.</h1>
  <div class="abs welcome-img" role="img" aria-label="Classical stock exchange facade with columns"></div>
  <p class="abs body-copy" style="left:392px;top:775px;width:450px">Lorem ipsum dolor sit amet, consectetur adipiscing elit. Proin pulvinar eros in imperdiet porttitor. Praesent velit justo, placerat ut ornare aliquet, venenatis vel justo. Nulla porttitor enim vitae nibh scelerisque, nec laoreet libero posu-ere. Integer ut neque ut purus dictum auctor. Cras tincidunt odio a pharetra iaculis. Nam in arcu eu tortor consequat tempor. Vivamus eu convallis risus.</p>
  <p class="abs body-copy" style="left:392px;top:879px">Mauris pulvinar, eros ac elementum tempus.</p>
  <p class="abs body-copy" style="left:136px;top:931px;width:700px">Lorem ipsum dolor sit amet, consectetur adipiscing elit. Proin pulvinar eros in imperdiet porttitor. Praesent velit justo, placerat ut ornare aliquet, venenatis vel justo. Nulla porttitor enimtempor. Vivamus eu convallis risus.</p>
  <span class="abs read-more">Read More</span>
</section>

<aside>
  <div class="abs ad-title">ADVERTISMENT</div>
  <div class="abs ad-img" role="img" aria-label="Bank advertisement with a glass dome over a savings box"></div>
  <span class="abs view-all">VIEW ALL</span>
</aside>

<footer class="abs footer"></footer>
<nav class="abs footer-nav">
  <a href="#">Home</a><a href="#">About Us</a><a href="#">Service</a><a href="#">Strength</a><a href="#">Partner</a><a href="#">News</a><a href="#">Contact US</a><a href="#">Blog</a>
</nav>
<p class="abs copyright">Copyright 2014, lorvextradelink.com &nbsp;|&nbsp; All Right Reserved.</p>
<div class="abs brand footer-brand"><span class="mark"></span><span class="name">LORVEX TRADE LINK</span></div>
</body>
</html>
```